Business Card design for law firm = Brindlecourt Australia

We are seeking a new design for our business cards.
We are keeping our logo, which is attached.
We need space for
Name
Title
Address is , which is
Level 14
83 Tarrenby Street
Sydney NSW 2000
Phone :
Mobile :
Fax :
Email :
DX :
website www.brindlecourt.com.au

Industry/Entity Type

Law Firm / Banking and Finance

Contact Information for Business Card

We are seeking a new design for our business cards. We are keeping our logo. We need space for Name Title Address is Level 14 83 Tarrenby Street Sydney NSW 2000 Phone Mobile Fax Email DX website www.brindlecourt.com.au

Colors
0054AA
0677BA
7BADD7
CADEEF
E8F1F8

Requirements
Must have
• see our website for general feel www.brindlecourt.com.au

```html
<!DOCTYPE html>
<html lang="en">
<head>
<meta charset="utf-8">
<title>Brindlecourt Australia — Business Card</title>
<link rel="stylesheet" href="https://fonts.googleapis.com/css2?family=Tinos:wght@400;700&display=swap">
<style>
  :root{
    --navy:#0054AA;
    --blue:#0677BA;
    --sky:#7BADD7;
    --mist:#CADEEF;
    --ice:#E8F1F8;
    --ink:#2b2f36;
    --page:#eceef1;
  }
  *{box-sizing:border-box;margin:0;padding:0}
  html,body{width:1200px;height:900px;overflow:hidden;background:var(--page)}
  body{font-family:"Tinos","Times New Roman",serif;color:var(--ink);position:relative}

  .card{
    position:absolute;left:320px;width:560px;height:320px;border-radius:26px;
    box-shadow:0 10px 30px rgba(20,40,70,.18);overflow:hidden;
  }
  .card--front{
    top:100px;
    background:radial-gradient(ellipse 75% 80% at 55% 45%,#ffffff 0%,#f4f8fb 45%,var(--ice) 70%,#a9cbe6 100%);
  }
  .card--back{top:480px;background:linear-gradient(135deg,#ffffff 0%,#f6f7f8 55%,#ffffff 100%)}

  .brand{position:absolute;margin:0}
  .brand__name{font-family:"Tinos","Times New Roman",serif;font-weight:400;color:var(--ink);text-transform:uppercase;letter-spacing:6px;line-height:1}

  .card--front .brand{left:50%;top:50%;transform:translate(-50%,-50%)}
  .card--front .brand__name{font-size:34px}

  .card--back .brand{right:34px;bottom:56px}
  .card--back .brand__name{font-size:24px;letter-spacing:4px}

  .divider{position:absolute;right:0;top:168px;width:250px;height:2px;background:var(--navy)}

  .person{position:absolute;left:30px;top:34px}
  .person__name{font-size:21px;font-weight:700;color:var(--navy);line-height:1.1}
  .person__title{font-size:15px;color:var(--ink);line-height:1.2}
  .person__mobile{display:flex;align-items:center;gap:8px;margin-top:10px;font-size:16px}

  .contact{position:absolute;left:290px;top:26px;list-style:none;font-size:14.5px;line-height:1.35}
  .contact li{display:flex;align-items:flex-start;gap:7px}
  .contact .indent{padding-left:19px}
  .contact .dx{color:var(--blue)}
  .icon{width:12px;height:12px;flex:none;margin-top:3px;fill:var(--blue)}
</style>
</head>
<body>

<section class="card card--front" aria-label="Card front">
  <p class="brand"><span class="brand__name">Brindlecourt</span></p>
</section>

<section class="card card--back" aria-label="Card back">
  <div class="person">
    <p class="person__name">Sam Ardley</p>
    <p class="person__title">Managing Director</p>
    <p class="person__mobile">
      <svg class="icon" viewBox="0 0 12 12" aria-hidden="true"><rect x="2.5" y="0.5" width="7" height="11" rx="1.2" fill="none" stroke="#0677BA" stroke-width="1.2"/><circle cx="6" cy="9.6" r=".7"/></svg>
      22 9184 5520
    </p>
  </div>

  <ul class="contact">
    <li><svg class="icon" viewBox="0 0 12 12" aria-hidden="true"><path d="M2.3 1l2 2.2-1 1.3c.8 1.6 2 2.8 3.4 3.5l1.3-1 2.2 2-1.3 1.6C5 10.3 1.6 7 .9 2.3z"/></svg>02 9184 0376</li>
    <li><svg class="icon" viewBox="0 0 12 12" aria-hidden="true"><rect x="3" y="1" width="6" height="4"/><rect x="1" y="5" width="10" height="5" rx="1"/><rect x="3" y="9" width="6" height="2" fill="#fff"/></svg>02 9184 0377</li>
    <li><svg class="icon" viewBox="0 0 12 12" aria-hidden="true"><rect x="1" y="2.5" width="10" height="7" rx="1"/><path d="M1.5 3l4.5 3.5L10.5 3" fill="none" stroke="#fff" stroke-width="1"/></svg>enquiries@brindlecourt.com.au</li>
    <li><svg class="icon" viewBox="0 0 12 12" aria-hidden="true"><circle cx="6" cy="6" r="5" fill="none" stroke="#0677BA" stroke-width="1.2"/><path d="M1 6h10M6 1c-2 2.5-2 7.5 0 10M6 1c2 2.5 2 7.5 0 10" fill="none" stroke="#0677BA" stroke-width=".9"/></svg>www.brindlecourt.com.au</li>
    <li><svg class="icon" viewBox="0 0 12 12" aria-hidden="true"><path d="M6 .5a3.8 3.8 0 0 0-3.8 3.8C2.2 7.2 6 11.5 6 11.5s3.8-4.3 3.8-7.2A3.8 3.8 0 0 0 6 .5zm0 5.2a1.4 1.4 0 1 1 0-2.8 1.4 1.4 0 0 1 0 2.8z"/></svg>Level 14, 83 Tarrenby Street</li>
    <li class="indent">Sydney NSW 2000</li>
    <li class="indent dx">DX 318 Sydney</li>
  </ul>

  <div class="divider"></div>

  <p class="brand"><span class="brand__name">Brindlecourt</span></p>
</section>

</body>
</html>
```